Doctors Office Web Design

Name of the business is Lian-Hua Qiu M.D.
We need a web design that is attractive for women that want to see Dr. Lian-Hua Qiu for Obstetrician Gynecology and Pregnancy care. Dr. Qiu earned her degree from Harbor Crest Medical College of obstetrician gynecology. We want to attract women of child bearing ages to come to our offices for health, education, and pregnancies.

Please visit http://www.drqiucare-example.com/ to help you get a feel for who we are. We will be adding some pictures and logo in the next few days.

We are looking for to have pages for and tabs including
About Us- History, Our Staff, Dr. Qiu
Patient Information- Appointments, E-Prescriptions, Payments Accepted, Insurance
Health- General, Sexual, Mental, Affiliates
Pregnancy- Minimally invasive surgery(our specialty), 4-D Ultra Sound, Hospital Affiliations
Media- News,Pictures, Videos
Locations- Palmvale Office, Marlow Office

The colors we would like to use are pastel colors, magenta, and plum

Target Market(s)

Women of all ages with an emphasis on 25-65 year olds

Industry/Entity Type

Business

Requirements
Must have
• Needs to include a location for a our videos and pictures that I will submit shortly. We also want a map to our location or atleast a place for one.
Nice to have
• A place for a google map of our office locations.

```html
<!DOCTYPE html>
<html lang="en">
<head>
<meta charset="utf-8">
<title>Lian-Hua Qiu M.D. – Obstetrician / Gynecologist</title>
<link href="https://fonts.googleapis.com/css2?family=Crimson+Text:wght@700&family=PT+Sans:ital,wght@0,400;0,700;1,400;1,700&family=Arimo:wght@400;700&display=swap" rel="stylesheet">
<style>
:root{
  --header-dark:#063355;
  --header-mid:#0e4d7d;
  --tab-top:#2f82be;
  --tab-bottom:#115690;
  --sub-band:#8fb8dc;
  --hero-title:#1f6e9e;
  --ink:#111;
  --grey-text:#555;
  --btn-blue:#47a6d9;
  --feature-blue:#1d8ccf;
  --green:#8dbb2a;
  --link-green:#6b9a12;
  --welcome-top:#f2f9fe;
  --welcome-bottom:#d6ecfa;
  --welcome-border:#9ccbe8;
  --magenta:#c0399c;
  --login-bg:#f2f2f2;
  --panel-bg:#fefde9;
  --panel-border:#e6e2b4;
  --olive:#5b5b2e;
  --olive-btn-top:#8a8a48;
  --olive-btn-bottom:#5c5c26;
  --footer-top:#e6f3fb;
  --footer-mid:#c4e3f5;
  --pill:#1aa3e0;
  --badge:#e4d6ea;
}
*{margin:0;padding:0;box-sizing:border-box}
html,body{width:958px;height:1200px;overflow:hidden;background:#fff}
body{position:relative;font-family:"PT Sans",Arial,sans-serif;color:var(--ink)}
.abs{position:absolute}

/* header */
.site-header{left:0;top:0;width:958px;height:113px;background:linear-gradient(180deg,var(--header-mid),var(--header-dark))}
.brand-name{left:20px;top:12px;font-family:"Crimson Text",Georgia,serif;font-weight:700;font-size:33px;color:#fff;letter-spacing:.5px;white-space:nowrap}
.brand-role{left:21px;top:56px;width:300px;height:15px;background:var(--sub-band);color:#fff;font-size:11px;line-height:15px;letter-spacing:6.1px;padding-left:3px;white-space:nowrap;overflow:hidden}
.social{top:12px;height:28px;font-size:11px;font-weight:700;color:#fff;line-height:28px;white-space:nowrap}
.social span{display:inline-block;width:8px;height:8px;background:#8fc6ea;margin-right:4px}
.main-nav{left:343px;top:80px;display:flex}
.main-nav a{height:33px;display:flex;align-items:center;justify-content:center;color:#fff;font-size:13px;text-decoration:none;background:linear-gradient(180deg,var(--tab-top),var(--tab-bottom));border-left:1px solid #5da3d6;border-right:1px solid #0a3e6a;white-space:nowrap}

/* hero */
.hero{left:0;top:113px;width:958px;height:295px;background:linear-gradient(90deg,#e6e6e6,#f6f6f6 55%,#ececec)}
.hero-photo{left:0;top:113px;width:530px;height:295px;background:radial-gradient(ellipse at 45% 70%,#c79a7c 0%,#e2cbb8 30%,#f2f2f2 70%)}
.hero-title{left:533px;top:155px;font-size:24px;font-weight:400;color:var(--hero-title);white-space:nowrap}
.hero-services{left:533px;top:214px;width:400px;font-size:21.5px;line-height:29px;color:var(--ink)}
.read-more{left:629px;top:332px;width:156px;height:35px;border-radius:3px;background:var(--btn-blue);color:#fff;font-size:24px;line-height:35px;text-align:center}

/* featured */
.featured-title{left:105px;top:441px;font-size:18px;font-weight:400;font-style:italic;color:var(--green)}
.featured-rule{left:105px;top:469px;width:150px;height:1px;background:#ccc}
.featured-list{left:105px;top:484px;width:136px;list-style:none}
.featured-list li{height:28.8px;border-bottom:1px solid #ddd;font-size:12px;font-style:italic;font-weight:700;color:var(--grey-text);display:flex;align-items:center;white-space:nowrap}
.featured-list li:last-child{border-bottom:none}
.featured-list svg{margin-right:7px}

.feature{width:160px}
.feature h3{position:absolute;left:43px;top:12px;font-size:14px;font-weight:400;color:var(--feature-blue);white-space:nowrap}
.feature p{position:absolute;top:44px;left:0;width:165px;font-size:10.5px;line-height:14.5px;color:#222;white-space:nowrap}
.feature a{position:absolute;top:73px;left:0;font-size:10.5px;color:var(--link-green)}

.welcome{left:314px;top:546px;width:557px;height:71px;border:1px solid var(--welcome-border);border-radius:5px;background:linear-gradient(180deg,var(--welcome-top),var(--welcome-bottom));padding:9px 10px;font-size:10.6px;line-height:17px;letter-spacing:-.1px;color:#111}
.welcome a{color:var(--magenta)}

/* login */
.login{left:88px;top:641px;width:171px;height:232px;background:var(--login-bg);border:1px solid #ddd;border-radius:6px}
.login h2{position:absolute;left:13px;top:16px;font-family:Arimo,Arial,sans-serif;font-size:17px;font-weight:700;color:#1a7db8}
.login label{position:absolute;left:13px;font-family:Arimo,Arial,sans-serif;font-size:10.5px;color:#333}
.field{position:absolute;background:#fff;border:1px solid #c8c8c8;border-radius:4px}
.login-btn{position:absolute;left:13px;top:137px;width:77px;height:25px;border:1px solid #bbb;border-radius:3px;background:linear-gradient(180deg,#fff,#ddd);font-family:Arimo,Arial,sans-serif;font-size:11px;font-weight:700;text-align:center;line-height:23px}
.login a{position:absolute;left:13px;font-family:Arimo,Arial,sans-serif;font-size:10.5px;color:#1a7db8;text-decoration:underline;white-space:nowrap}

/* info panel */
.info{left:266px;top:641px;width:605px;height:232px;background:var(--panel-bg);border:1px solid var(--panel-border);border-radius:4px}
.info h2{position:absolute;top:11px;font-family:Arimo,Arial,sans-serif;font-weight:400;font-size:16px;color:var(--olive);white-space:nowrap}
.address{position:absolute;left:16px;font-family:Arimo,Arial,sans-serif;font-size:12px;line-height:14.4px;color:#111;white-space:nowrap}
.input{position:absolute;left:211px;width:161px;background:#fff;border:1px solid #ccc;border-radius:5px;font-family:Arimo,Arial,sans-serif;font-size:9.5px;color:#999;padding:5px 8px}
.send{position:absolute;left:318px;top:197px;width:54px;height:23px;border-radius:4px;background:linear-gradient(180deg,var(--olive-btn-top),var(--olive-btn-bottom));color:#fff;font-family:Arimo,Arial,sans-serif;font-size:10.5px;text-align:center;line-height:23px}
.map{position:absolute;left:422px;top:43px;width:164px;height:138px;border:1px solid #999;background:linear-gradient(135deg,#e9e5dc,#d9d5cc 50%,#ebe6c8)}
.view-map{position:absolute;left:537px;top:197px;font-family:Arimo,Arial,sans-serif;font-size:11px;color:#111;text-decoration:underline}

/* footer */
.footer-band{left:0;top:928px;width:958px;height:205px;background:linear-gradient(180deg,#fff 0%,var(--footer-top) 12%,var(--footer-mid) 55%,var(--footer-top) 88%,#fff 100%)}
.footer-col{top:994px}
.footer-col h4{width:96px;height:18px;border-radius:3px;background:var(--pill);color:#fff;font-size:10.5px;font-weight:400;line-height:18px;padding-left:8px;white-space:nowrap}
.footer-col ul{list-style:none;margin-top:13px;margin-left:8px}
.footer-col li{font-size:10.2px;line-height:14.5px;color:#222;white-space:nowrap}
.footer-col li::before{content:"›";margin-right:6px;font-weight:700}
.badge{left:732px;top:982px;width:80px;height:100px;border-radius:6px;background:var(--badge)}
.contact{left:0;top:1147px;width:958px;text-align:center;font-size:11px;color:#111}
.contact a{color:var(--magenta);text-decoration:none}
.copyright{left:0;top:1173px;width:958px;text-align:center;font-size:11px;color:#111}
</style>
</head>
<body>

<header class="abs site-header"></header>
<div class="abs brand-name">Lian-Hua Qiu M.D.</div>
<div class="abs brand-role">Obstetrician/Gynecologist</div>
<div class="abs social" style="left:806px"><span></span>Circlo</div>
<div class="abs social" style="left:853px"><span></span>Chirra</div>
<div class="abs social" style="left:898px"><span></span>Feedline</div>
<nav class="abs main-nav">
  <a style="width:80px">Home</a>
  <a style="width:80px">About Us</a>
  <a style="width:128px">Patient Information</a>
  <a style="width:78px">Health</a>
  <a style="width:80px">Pregnancy</a>
  <a style="width:79px">Media</a>
  <a style="width:78px">Locations</a>
</nav>

<section class="abs hero"></section>
<div class="abs hero-photo" role="img" aria-label="Photo of an expectant mother holding her belly with baby shoes resting on it"></div>
<h1 class="abs hero-title">Serving All Areas of Women's Health</h1>
<p class="abs hero-services">Obstetrics, Family Planning, Hormonal Evaluation, Incontinence, Infertility, and Gynecology Surgery</p>
<div class="abs read-more">Read More</div>

<h2 class="abs featured-title">Featured Services</h2>
<div class="abs featured-rule"></div>
<svg class="abs" style="left:132px;top:469px" width="16" height="9"><path d="M0 0 L8 8 L16 0" fill="#fff" stroke="#ccc"/></svg>
<ul class="abs featured-list">
  <li><svg width="11" height="11"><circle cx="5.5" cy="5.5" r="5" fill="#e4e4e4" stroke="#bbb"/><path d="M4.5 3 L7.5 5.5 L4.5 8Z" fill="#777"/></svg>Health Tips</li>
  <li><svg width="11" height="11"><circle cx="5.5" cy="5.5" r="5" fill="#e4e4e4" stroke="#bbb"/><path d="M4.5 3 L7.5 5.5 L4.5 8Z" fill="#777"/></svg>Women Care</li>
  <li><svg width="11" height="11"><circle cx="5.5" cy="5.5" r="5" fill="#e4e4e4" stroke="#bbb"/><path d="M4.5 3 L7.5 5.5 L4.5 8Z" fill="#777"/></svg>Child Care</li>
  <li><svg width="11" height="11"><circle cx="5.5" cy="5.5" r="5" fill="#e4e4e4" stroke="#bbb"/><path d="M4.5 3 L7.5 5.5 L4.5 8Z" fill="#777"/></svg>Speak to a Doctor</li>
  <li><svg width="11" height="11"><circle cx="5.5" cy="5.5" r="5" fill="#e4e4e4" stroke="#bbb"/><path d="M4.5 3 L7.5 5.5 L4.5 8Z" fill="#777"/></svg>Free Dial Numbers</li>
</ul>

<div class="abs feature" style="left:314px;top:446px">
  <svg class="abs" width="34" height="36"><rect x="2" y="1" width="24" height="32" fill="#fff" stroke="#999"/><circle cx="18" cy="20" r="7" fill="#dbeefa" stroke="#555" stroke-width="2"/><path d="M23 25 L31 33" stroke="#555" stroke-width="3"/></svg>
  <h3>Find a Specialist</h3>
  <p>Lorem Ipsum is simply dummy text<br>&nbsp;of the printing and typesetting</p>
  <a>click here...</a>
</div>
<div class="abs feature" style="left:526px;top:446px">
  <svg class="abs" width="34" height="36"><path d="M4 30 L22 2 L30 6 L14 34Z" fill="#2a6fb8"/><path d="M2 33 L30 33" stroke="#999" stroke-width="2"/></svg>
  <h3 style="top:16px">Patient Stories</h3>
  <p>Lorem Ipsum is simply dummy text<br>of the printing and typesetting</p>
  <a>click here...</a>
</div>
<div class="abs feature" style="left:717px;top:446px">
  <svg class="abs" width="34" height="38"><rect x="1" y="1" width="32" height="28" fill="#eee" stroke="#888"/><circle cx="17" cy="15" r="10" fill="#3da843"/><path d="M17 8 V19 M12 15 L17 20 L22 15" stroke="#fff" stroke-width="2.5" fill="none"/><rect x="3" y="30" width="28" height="6" fill="#bbb"/></svg>
  <h3 style="top:16px">Get Involved</h3>
  <p>Lorem Ipsum is simply dummy text<br>of the printing and typesetting</p>
  <a>click here...</a>
</div>

<div class="abs welcome">Welcome to Dr. Lian-Hua Qiu's website. Here you will be able to find information about both of our offices, meet Dr. Qiu and her staff, and browse through our women's health links to learn more about pregnancy, nutrition, exercise, and other women's health issues. Have fun and if you have any questions, feel free to contact us at <a>drqiu@qiucaremail.com</a></div>

<section class="abs login">
  <h2>User Login</h2>
  <label style="top:47px">User Name</label>
  <div class="field" style="left:13px;top:60px;width:146px;height:20px"></div>
  <label style="top:89px">Password</label>
  <div class="field" style="left:13px;top:101px;width:146px;height:20px"></div>
  <div class="login-btn">Login</div>
  <a style="top:179px">Create new account</a>
  <a style="top:199px">Request new password</a>
</section>

<section class="abs info">
  <h2 style="left:16px">Our Locations</h2>
  <p class="address" style="top:44px">2210 Lantern Bay Road<br>Suite 210-211<br>Marlow, Florida&nbsp; 33480<br>Tel:&nbsp; (555) 410-2236<br>Fax: (555) 410-2237</p>
  <p class="address" style="top:137px">2210 Lantern Bay Road<br>Suite 210-211<br>Marlow, Florida&nbsp; 33480<br>Tel:&nbsp; (555) 410-2236<br>Fax: (555) 410-2237</p>

  <h2 style="left:213px">Schedule Appointment</h2>
  <div class="input" style="top:41px;height:23px">Name:</div>
  <div class="input" style="top:70px;height:23px">Email:</div>
  <div class="input" style="top:99px;height:23px">Phone:</div>
  <div class="input" style="top:130px;height:55px">Message:</div>
  <div class="send">Send</div>

  <h2 style="left:422px">Directions</h2>
  <div class="map" role="img" aria-label="Street map showing the office location"></div>
  <div class="view-map">View Map</div>
</section>

<div class="abs footer-band"></div>
<div class="abs footer-col" style="left:104px">
  <h4>Main Navigation</h4>
  <ul><li>Home</li><li>Profile</li><li>Services</li><li>About Us</li></ul>
</div>
<div class="abs footer-col" style="left:238px">
  <h4>For Patients</h4>
  <ul><li>My Health Portal</li><li>Visitors Guide</li><li>Greeter Program</li><li>Making Appointments</li></ul>
</div>
<div class="abs footer-col" style="left:376px">
  <h4>My Health</h4>
  <ul><li>Request appointments</li><li>Subscribe to health information</li><li>Join or start a support group</li></ul>
</div>
<div class="abs footer-col" style="left:548px">
  <h4>Useful Links</h4>
  <ul><li>brightharbor.org</li><li>marlowunitedcare.org</li><li>sunnytown.info</li><li>coastalrecovery.org</li></ul>
</div>
<div class="abs badge" role="img" aria-label="Awareness month partner badge"></div>

<p class="abs contact">Contact us!&nbsp; Send e-mail to <a>drqiu@qiucaremail.com</a> with your comments and suggestions for this site.</p>
<p class="abs copyright">(c) Copyright 2002, Lian-Hua Qiu, M.D., P.A.</p>

</body>
</html>
```